Real Estate Investing company needs a business card design

We need a business card design for new Real Estate Investment Company called "Maple Ridge Ventures, LLC." We buy homes for cash and close quickly in any situation. Our company provides an easy and fast option for home owners who are in tough situations who need to sell their home fast and don't want realtor fees or other listing hassles. We also renovate and resell our homes which helps provide housing for the community. We would like to see designs that use the colors blue and white to match our company logo or other colors that may match our company logo. The final design should communicate trust and easy process.
Industry/Entity Type
Business
Contact Information for Business Card
Front should have company name and company logo. back of card should have company logo and area to list services.
Look and feel

```html
<!DOCTYPE html>
<html lang="en">
<head>
<meta charset="utf-8">
<title>Maple Ridge Ventures – Business Card</title>
<link href="https://fonts.googleapis.com/css2?family=Open+Sans:wght@400;600;700&display=swap" rel="stylesheet">
<style>
  :root {
    --canvas: #e6e4e1;
    --card: #2a2a2b;
    --blue: #1f73c4;
    --white: #ffffff;
    --band: #efefef;
    --ink: #2a2a2b;
    --emboss: #3a3a3c;
  }
  * { margin: 0; padding: 0; box-sizing: border-box; }
  html, body { width: 1200px; height: 1000px; overflow: hidden; }
  body {
    background: var(--canvas);
    font-family: "Open Sans", Arial, sans-serif;
    position: relative;
  }
  .card {
    position: absolute;
    left: 265px;
    width: 665px;
    height: 397px;
    background: var(--card);
    box-shadow: 0 6px 14px rgba(0,0,0,0.25);
    overflow: hidden;
  }
  .card--front { top: 73px; }
  .card--back { top: 532px; height: 398px; }

  .brand {
    position: absolute;
    left: 34px;
    top: 52px;
    display: flex;
    align-items: center;
    gap: 14px;
    color: var(--blue);
    font-weight: 700;
    font-size: 36px;
    line-height: 1.05;
    letter-spacing: 0.5px;
  }
  .brand__mark { width: 22px; height: 22px; background: var(--blue); flex: none; }

  .person { position: absolute; left: 32px; top: 202px; color: var(--white); }
  .person__name { color: var(--blue); font-weight: 700; font-size: 21px; letter-spacing: 0.3px; }
  .person__title { font-size: 16px; margin-top: 2px; }

  .contact { position: absolute; left: 32px; top: 274px; list-style: none; color: var(--white); font-size: 16px; }
  .contact li { display: flex; align-items: center; height: 24.5px; }
  .contact svg { width: 14px; height: 14px; margin-right: 11px; fill: var(--blue); }

  .services { position: absolute; left: 408px; top: 172px; color: var(--white); }
  .services__title { color: var(--blue); font-weight: 700; font-size: 18px; margin-bottom: 3px; }
  .services__list { list-style: none; font-size: 15.5px; }
  .services__list li { display: flex; align-items: center; height: 22.2px; }
  .services__list svg { width: 14px; height: 12px; margin-right: 7px; }

  .footer-wave { position: absolute; left: 0; bottom: 0; width: 665px; height: 50px; }
  .website {
    position: absolute; right: 32px; bottom: 8px;
    color: var(--ink); font-size: 16px;
  }

  .brand--back {
    position: absolute; left: 0; right: 0; top: 148px;
    text-align: center;
    color: var(--emboss);
    font-weight: 700;
    font-size: 46px;
    line-height: 1.05;
    letter-spacing: 1px;
  }
</style>
</head>
<body>
  <section class="card card--front">
    <div class="brand">
      <span class="brand__mark"></span>
      <span class="brand__name">MAPLE RIDGE<br>VENTURES</span>
    </div>

    <div class="person">
      <p class="person__name">DANIEL HAYES</p>
      <p class="person__title">Chief Executive Officer</p>
    </div>

    <ul class="contact">
      <li><svg viewBox="0 0 14 14"><rect x="3.5" y="0" width="7" height="14" rx="1.5"/></svg>+ 000 000 0000</li>
      <li><svg viewBox="0 0 14 14"><rect x="3" y="0" width="8" height="4"/><rect x="0" y="5" width="14" height="6" rx="1"/><rect x="3" y="9" width="8" height="5"/></svg>+ 000 000 0000</li>
      <li><svg viewBox="0 0 14 14"><path d="M0 3h14v8H0z"/><path d="M0 3l7 5 7-5" stroke="#2a2a2b" stroke-width="1.2" fill="none"/></svg>info@mapleridgeventures.com</li>
    </ul>

    <div class="services">
      <p class="services__title">SERVICES</p>
      <ul class="services__list">
        <li><svg viewBox="0 0 14 12"><path d="M1 6l4 4 8-9" stroke="#1f73c4" stroke-width="2" fill="none"/></svg>Lead Generation</li>
        <li><svg viewBox="0 0 14 12"><path d="M1 6l4 4 8-9" stroke="#1f73c4" stroke-width="2" fill="none"/></svg>Customer Acquisition</li>
        <li><svg viewBox="0 0 14 12"><path d="M1 6l4 4 8-9" stroke="#1f73c4" stroke-width="2" fill="none"/></svg>Internet Marketing</li>
        <li><svg viewBox="0 0 14 12"><path d="M1 6l4 4 8-9" stroke="#1f73c4" stroke-width="2" fill="none"/></svg>Phone Verified Leads</li>
        <li><svg viewBox="0 0 14 12"><path d="M1 6l4 4 8-9" stroke="#1f73c4" stroke-width="2" fill="none"/></svg>Performance Analytics</li>
        <li><svg viewBox="0 0 14 12"><path d="M1 6l4 4 8-9" stroke="#1f73c4" stroke-width="2" fill="none"/></svg>Inbound Services</li>
      </ul>
    </div>

    <svg class="footer-wave" viewBox="0 0 665 50" preserveAspectRatio="none">
      <path d="M0 50 C180 20 360 6 665 14 L665 50 Z" fill="#efefef"/>
      <path d="M0 40 C150 16 320 4 480 4 C320 10 160 26 0 46 Z" fill="#1f73c4"/>
      <path d="M0 50 C160 30 330 14 520 10 C330 20 170 36 30 50 Z" fill="#111"/>
    </svg>
    <p class="website">www.mapleridgeventures.com</p>
  </section>

  <section class="card card--back">
    <p class="brand--back">MAPLE RIDGE<br>VENTURES</p>
  </section>
</body>
</html>
```